We need a fresh, new church business card!!

We need a church business card with basic info to hand out as invites. We are looking for something clean that communicates our basic information clearly.

We are open to square or rectangle card sizes.

General Public

Religious

The attached logo is the only one that I have available. We'd like to see options with with text of the logo lighter and on a dark background as well as options with white/light backgrounds.

Also, we'd like to see option with rounded corners.

• Address - 2718 Maple Row, Rockford, IL 61142
• Website - brookvane.example
• Phone - 815-555-0163
• Service times -
• Sunday - 10am Sunday School
• - 11am Family Worship
• - 6pm Night of Prayer
• Wednesday - 7:30pm Adult Bible Study
• Classes for all ages

```html
<!DOCTYPE html>
<html lang="en">
<head>
<meta charset="utf-8">
<title>Brookvane Pentecostal Church – Business Card</title>
<link rel="stylesheet" href="https://fonts.googleapis.com/css2?family=Roboto+Slab:wght@300;400;600&display=swap">
<style>
  :root {
    --backdrop: #a3a1a1;
    --card: #ffffff;
    --teal: #5e96a7;
    --teal-dark: #4f8798;
    --swoosh: #7d7d7f;
    --ink: #76777a;
    --ink-dark: #5f6063;
  }
  * { margin: 0; padding: 0; box-sizing: border-box; }
  html, body { width: 1200px; height: 1200px; overflow: hidden; }
  body {
    background: var(--backdrop);
    position: relative;
    font-family: "Roboto Slab", Georgia, serif;
    color: var(--ink);
  }
  .card {
    position: absolute;
    width: 712px;
    height: 418px;
    background: var(--card);
    border-radius: 28px;
    overflow: hidden;
  }
  .card-front { left: 238px; top: 119px; }
  .card-back  { left: 230px; top: 644px; }

  /* church name lockup */
  .name-lockup { position: absolute; display: flex; align-items: center; }
  .name-dot { border-radius: 50%; background: var(--teal); flex: none; }
  .name-text { color: var(--ink); font-weight: 400; line-height: 1; }
  .name-main { display: block; }
  .name-sub { display: block; text-transform: uppercase; }

  .card-front .name-lockup { left: 127px; top: 152px; }
  .card-front .name-dot { width: 84px; height: 84px; margin-right: 26px; }
  .card-front .name-main { font-size: 56px; letter-spacing: 1px; }
  .card-front .name-sub { font-size: 18px; letter-spacing: 5.4px; margin-top: 12px; }

  .card-back .name-lockup { left: 394px; top: 308px; }
  .card-back .name-dot { width: 46px; height: 46px; margin-right: 16px; }
  .card-back .name-main { font-size: 31px; letter-spacing: 0.5px; }
  .card-back .name-sub { font-size: 11px; letter-spacing: 3.1px; margin-top: 6px; }

  .wave { position: absolute; left: 0; top: 0; }

  .contact-list {
    position: absolute;
    right: 26px;
    top: 38px;
    list-style: none;
    color: #ffffff;
    font-weight: 300;
    font-size: 18px;
    text-align: right;
  }
  .contact-list li { display: flex; justify-content: flex-end; align-items: center; height: 26.5px; }
  .contact-icon { width: 17px; height: 17px; margin-left: 10px; fill: #ffffff; }

  .service-times { position: absolute; left: 45px; top: 126px; }
  .service-title {
    display: inline-block;
    border: 2px solid var(--teal);
    padding: 3px 16px 2px;
    font-size: 19px;
    font-weight: 400;
    color: var(--ink-dark);
    letter-spacing: 0.5px;
  }
  .service-day {
    margin-top: 16px;
    font-size: 17.5px;
    font-weight: 600;
    color: var(--teal);
    line-height: 1.2;
  }
  .service-day + .service-list { margin-top: 2px; }
  .service-list + .service-day { margin-top: 0; }
  .service-list { list-style: none; font-size: 17.5px; font-weight: 300; line-height: 26.5px; color: var(--ink); }
  .classes-note {
    position: absolute;
    left: 43px;
    top: 354px;
    font-size: 17.5px;
    font-weight: 600;
    color: var(--teal);
  }
</style>
</head>
<body>

<section class="card card-front" aria-label="Card front">
  <div class="name-lockup">
    <span class="name-dot"></span>
    <span class="name-text">
      <span class="name-main">BROOKVANE</span>
      <span class="name-sub">Pentecostal Church</span>
    </span>
  </div>
</section>

<section class="card card-back" aria-label="Card back">
  <svg class="wave" width="712" height="418" viewBox="0 0 712 418" aria-hidden="true">
    <path fill="var(--teal)" d="M0,0 H712 V198 C610,186 530,160 440,118 C340,72 200,38 0,58 Z"/>
    <path fill="var(--swoosh)" d="M0,66 C190,40 330,62 440,120 C530,166 610,192 712,204 V226 C610,212 530,190 440,146 C340,100 190,62 0,84 Z"/>
    <path fill="#ffffff" d="M0,58 C200,38 340,72 440,118 C530,160 610,186 712,198 V204 C610,192 530,166 440,120 C330,62 190,40 0,66 Z"/>
    <path fill="var(--swoosh)" d="M70,80 C170,64 270,68 360,94 C270,78 170,76 70,82 Z"/>
  </svg>

  <ul class="contact-list">
    <li>2718 Maple Row, Rockford, IL 61142
      <svg class="contact-icon" viewBox="0 0 20 20" aria-hidden="true"><path d="M2,8 C2,4 18,4 18,8 L15,9 L14,7 C12,6 8,6 6,7 L5,9 Z M5,10 L15,10 L17,17 L3,17 Z"/><circle cx="10" cy="13" r="2" fill="var(--teal)"/></svg>
    </li>
    <li>www.brookvane.example
      <svg class="contact-icon" viewBox="0 0 20 20" aria-hidden="true"><path d="M2,4 H18 V16 H2 Z"/><path d="M2,4 L10,11 L18,4" fill="none" stroke="var(--teal)" stroke-width="1.6"/></svg>
    </li>
    <li>815-555-0163
      <svg class="contact-icon" viewBox="0 0 20 20" aria-hidden="true"><path d="M10,1 C6,1 4,4 4,7 C4,11 10,19 10,19 C10,19 16,11 16,7 C16,4 14,1 10,1 Z"/><circle cx="10" cy="7" r="2.3" fill="var(--teal)"/></svg>
    </li>
  </ul>

  <div class="service-times">
    <h2 class="service-title">SERVICE TIMES</h2>
    <h3 class="service-day">SUNDAY</h3>
    <ul class="service-list">
      <li>Sunday School ..... 10:00am</li>
      <li>Family Worship .... 11:00am</li>
      <li>Night of Prayer ...... 6:00pm</li>
    </ul>
    <h3 class="service-day">WEDNESDAY</h3>
    <ul class="service-list">
      <li>Adult Bible Study ... 7:30pm</li>
    </ul>
  </div>
  <p class="classes-note">CLASSES FOR ALL AGES</p>

  <div class="name-lockup">
    <span class="name-dot"></span>
    <span class="name-text">
      <span class="name-main">BROOKVANE</span>
      <span class="name-sub">Pentecostal Church</span>
    </span>
  </div>
</section>

</body>
</html>
```